Web Design for Financial Consulting Company

We need a website design for a financial consulting company "Kelvane Consulting". We build financial models, scenario analysis, handle the budgeting process and provide temporary staffing. I have over 10 years of experience. My Excel expertise and analytical savvy has saved clients over $17 million in profit.

Target Market(s)

Small to medium businesses

Industry/Entity Type

Financial Consulting

Number of Pages Required

4 page

Requirements
Must have
• Professional looking
Nice to have
• A little futuristic looking

```html
<!DOCTYPE html>
<html lang="en">
<head>
<meta charset="utf-8">
<title>Kelvane Consulting</title>
<link href="https://fonts.googleapis.com/css2?family=IBM+Plex+Sans:wght@400;500;600;700&family=Lato:wght@400;700&display=swap" rel="stylesheet">
<style>
:root{
  --blue:#00a8f3;
  --blue-light:#b3e3fb;
  --blue-pale:#d6f0fc;
  --navy:#0d3350;
  --ink:#16232f;
  --dark:#1a2530;
  --black:#000;
  --text:#222;
  --muted:#666;
  --grey-bg:#f4f4f4;
  --white:#fff;
}
*{box-sizing:border-box;margin:0;padding:0}
html,body{width:1200px;height:3201px;overflow:hidden}
body{position:relative;background:var(--white);font-family:'Lato',sans-serif;color:var(--text)}
.abs{position:absolute}
.head{font-family:'IBM Plex Sans',sans-serif}

/* header */
.topbar{left:0;top:0;width:1200px;height:46px}
.topbar-info{top:0;left:520px;height:46px;display:flex;align-items:center;gap:42px;color:var(--white);font-size:16px;font-family:'IBM Plex Sans',sans-serif}
.topbar-info span{display:flex;align-items:center;gap:9px}
.brand{left:111px;top:38px;display:flex;align-items:center;gap:12px}
.brand-mark{width:46px;height:46px;border:4px solid var(--blue)}
.brand-name{font-family:'IBM Plex Sans',sans-serif;font-weight:700;font-size:34px;color:var(--navy);letter-spacing:1px;line-height:1}
.nav{left:616px;top:72px;display:flex;gap:37px;font-size:15px;font-family:'IBM Plex Sans',sans-serif;color:var(--text)}
.header-line{left:0;top:117px;width:1200px;height:1px;background:#e5e5e5}

/* hero */
.hero-title{left:112px;top:298px;font-family:'IBM Plex Sans',sans-serif;font-weight:700;font-size:76px;color:var(--white);letter-spacing:2px;line-height:1}
.hero-tag{left:112px;top:383px;height:52px;padding:0 14px;background:var(--blue);font-family:'IBM Plex Sans',sans-serif;font-weight:700;font-size:50px;line-height:52px;color:var(--white);letter-spacing:1px}
.hero-sub{left:113px;top:452px;font-size:16px;color:var(--white)}
.btn{display:flex;align-items:center;justify-content:center;background:var(--blue);color:var(--white);font-family:'IBM Plex Sans',sans-serif;font-weight:700;font-size:16px;border-radius:5px;letter-spacing:.5px}
.hero-btn{left:111px;top:494px;width:160px;height:51px}

/* services */
.section-title{width:1200px;left:0;text-align:center;font-family:'IBM Plex Sans',sans-serif;font-weight:700;font-size:36px;color:var(--black);letter-spacing:1px}
.service{text-align:center}
.service-icon{width:72px;height:72px;border-radius:50%;margin:0 auto;background:var(--blue-pale);display:flex;align-items:center;justify-content:center}
.service h3{font-family:'IBM Plex Sans',sans-serif;font-weight:600;font-size:22px;color:var(--black);margin-top:20px;line-height:26px}
.service .bar{width:38px;height:4px;background:var(--blue);margin:12px auto 24px}
.service p{font-size:13.5px;line-height:26px;color:var(--muted)}
.service .more{display:inline-flex;align-items:center;gap:5px;margin-top:18px;color:var(--blue);font-family:'IBM Plex Sans',sans-serif;font-weight:600;font-size:16px}
.service-featured{left:440px;top:929px;width:324px;height:341px;border-radius:44px;background:var(--white);box-shadow:0 8px 30px rgba(0,0,0,.09);padding:34px 28px 0}
.service-featured .service-icon{background:var(--blue)}
.arrow{width:20px;height:20px;border-radius:50%;display:flex;align-items:center;justify-content:center}

/* about */
.about-bg{left:0;top:1388px;width:1200px;height:608px;background:var(--grey-bg)}
.exp-panel{left:109px;top:1460px;width:452px;height:451px}
.exp-num{left:144px;top:1505px;font-family:'IBM Plex Sans',sans-serif;font-weight:700;font-size:92px;color:var(--white);line-height:1}
.exp-label{left:146px;top:1606px;font-family:'IBM Plex Sans',sans-serif;font-weight:700;font-size:36px;color:var(--white);line-height:42px}
.profit{left:447px;top:1794px;width:144px;height:144px;border-radius:50%;background:var(--dark);color:var(--white);font-family:'IBM Plex Sans',sans-serif;font-weight:700;padding:30px 0 0 40px}
.profit b{display:block;font-size:34px;line-height:36px}
.profit span{display:block;font-size:19px;line-height:24px}
.about-title{left:617px;top:1470px;font-family:'IBM Plex Sans',sans-serif;font-weight:700;font-size:35px;line-height:41px;color:var(--black);letter-spacing:1px}
.about-quote{left:615px;top:1585px;width:457px;height:164px;background:var(--white);border-left:8px solid var(--blue);border-radius:6px;box-shadow:0 6px 24px rgba(0,0,0,.07);padding:28px 20px 0 22px;font-size:13.5px;line-height:26px;color:var(--text)}
.about-btn{left:615px;top:1776px;width:171px;height:60px}

/* contact */
.contact-item{left:110px;display:flex;gap:14px}
.contact-icon{width:50px;height:50px;border-radius:50%;border:2px solid var(--blue);display:flex;align-items:center;justify-content:center;flex-shrink:0}
.contact-item h4{font-family:'IBM Plex Sans',sans-serif;font-weight:600;font-size:22px;color:var(--black);line-height:26px}
.contact-item p{font-size:15px;line-height:24px;color:var(--text);margin-top:4px}
.field{left:434px;width:317px;height:52px;background:var(--white);box-shadow:0 2px 12px rgba(0,0,0,.06);padding:0 24px;display:flex;align-items:center;font-size:15px;color:#777}
.field-message{left:771px;top:2168px;width:318px;height:257px;align-items:flex-start;padding-top:18px}
.submit{left:433px;top:2371px;width:318px;height:54px;border-radius:0}

/* footer */
.footer-logo{left:0;width:1200px;top:2858px;display:flex;justify-content:center;align-items:center;gap:16px}
.footer-logo .brand-mark{width:70px;height:70px;border-width:5px}
.footer-logo .brand-name{color:var(--white);font-size:58px}
.footer-links{left:0;width:1200px;top:2978px;display:flex;justify-content:center;gap:44px;font-size:16px;color:var(--white);font-family:'IBM Plex Sans',sans-serif}
.copyright{left:0;width:1200px;top:3035px;text-align:center;font-size:13px;color:var(--white);font-family:'IBM Plex Sans',sans-serif}
.copyright u{color:var(--blue)}
.socials{left:0;width:1200px;top:3086px;display:flex;justify-content:center;gap:8px}
.socials span{width:44px;height:44px;border-radius:50%;background:var(--white)}
.socials span:first-child{background:var(--blue)}
</style>
</head>
<body>

<!-- top contact bar -->
<svg class="abs topbar" width="1200" height="46" viewBox="0 0 1200 46"><polygon points="458,0 1200,0 1200,46 484,46" fill="var(--ink)"/></svg>
<div class="abs topbar-info">
  <span><svg width="15" height="15" viewBox="0 0 24 24"><path d="M6.6 10.8a15 15 0 006.6 6.6l2.2-2.2a1 1 0 011-.25 11.4 11.4 0 003.6.57 1 1 0 011 1V20a1 1 0 01-1 1A17 17 0 013 4a1 1 0 011-1h3.5a1 1 0 011 1c0 1.25.2 2.45.57 3.57a1 1 0 01-.25 1z" fill="#fff"/></svg>+1 555 014 2290</span>
  <span><svg width="15" height="12" viewBox="0 0 24 18"><rect width="24" height="18" rx="2" fill="#fff"/><path d="M1 2l11 8 11-8" stroke="var(--ink)" stroke-width="2" fill="none"/></svg>info@kelvaneconsulting.com</span>
  <span><svg width="14" height="14" viewBox="0 0 24 24"><path d="M10 5l7 7-7 7v-4H2V9h8zM14 3h7v18h-7v-2h5V5h-5z" fill="#fff"/></svg>Login</span>
</div>

<header>
  <div class="abs brand"><div class="brand-mark"></div><div class="brand-name">KELVANE</div></div>
  <nav class="abs nav"><span>Home</span><span>About</span><span>Our Services</span><span>Contact Us</span></nav>
  <div class="abs header-line"></div>
</header>

<!-- hero -->
<svg class="abs" style="left:0;top:118px" width="1200" height="666" viewBox="0 118 1200 666">
  <defs>
    <linearGradient id="heroPhoto" x1="0" y1="0" x2="1" y2="1">
      <stop offset="0" stop-color="#6a7479"/>
      <stop offset=".45" stop-color="#4a5a62"/>
      <stop offset="1" stop-color="#2b3a44"/>
    </linearGradient>
  </defs>
  <polygon role="img" aria-label="Photo of three smiling colleagues discussing documents in a bright office" points="0,118 1200,118 1200,186 0,783" fill="url(#heroPhoto)"/>
  <polygon points="503,534 1200,186 1200,739 503,739" fill="var(--blue)"/>
</svg>
<h1 class="abs hero-title">WELCOME TO</h1>
<div class="abs hero-tag">KELVANE CONSULTING</div>
<p class="abs hero-sub">Helping your finance team and increasing profit</p>
<div class="abs btn hero-btn">GET STARTED</div>

<!-- services -->
<h2 class="abs section-title" style="top:835px">OUR SERVICES</h2>

<div class="abs arrow" style="left:57px;top:1101px;background:var(--blue)"><svg width="8" height="8" viewBox="0 0 10 10"><path d="M7 1L3 5l4 4" stroke="#fff" stroke-width="2" fill="none"/></svg></div>
<div class="abs arrow" style="left:1127px;top:1101px;background:#ccc"><svg width="8" height="8" viewBox="0 0 10 10"><path d="M3 1l4 4-4 4" stroke="#fff" stroke-width="2" fill="none"/></svg></div>

<div class="abs service" style="left:146px;top:972px;width:260px">
  <div class="service-icon"><svg width="34" height="34" viewBox="0 0 34 34" fill="none" stroke="var(--blue)" stroke-width="1.5"><rect x="11" y="11" width="12" height="12"/><circle cx="5" cy="5" r="2.5"/><circle cx="29" cy="5" r="2.5"/><circle cx="5" cy="29" r="2.5"/><circle cx="29" cy="29" r="2.5"/><path d="M7 7l4 4M27 7l-4 4M7 27l4-4M27 27l-4-4"/></svg></div>
  <h3>Financial Models<br>– Projects:</h3>
  <div class="bar"></div>
  <p>Financial analysis, scenario modeling,<br>pricing analysis, projects</p>
  <div class="more">Learn More <svg width="14" height="14" viewBox="0 0 14 14"><circle cx="7" cy="7" r="7" fill="var(--blue)"/><path d="M5 4l3 3-3 3" stroke="#fff" stroke-width="2" fill="none"/></svg></div>
</div>

<div class="abs service service-featured">
  <div class="service-icon"><svg width="36" height="36" viewBox="0 0 36 36" fill="none" stroke="#fff" stroke-width="1.6"><rect x="4" y="8" width="24" height="17"/><path d="M16 25v5M10 30h12M8 20l5-5 4 3 6-7"/><path d="M26 4l6 6-3 3-6-6z"/></svg></div>
  <h3>Budgeting Process</h3>
  <div class="bar"></div>
  <p>Building budgets from scratch, revamping<br>current process to be more robust and<br>scalable.</p>
  <div class="more">Learn More <svg width="14" height="14" viewBox="0 0 14 14"><circle cx="7" cy="7" r="7" fill="var(--blue)"/><path d="M5 4l3 3-3 3" stroke="#fff" stroke-width="2" fill="none"/></svg></div>
</div>

<div class="abs service" style="left:788px;top:972px;width:280px">
  <div class="service-icon"><svg width="36" height="36" viewBox="0 0 36 36" fill="none" stroke="var(--blue)" stroke-width="1.6"><circle cx="15" cy="15" r="9"/><path d="M22 22l9 9"/><circle cx="15" cy="13" r="3"/><path d="M10 20c1-3 3-4 5-4s4 1 5 4"/></svg></div>
  <h3>Temporary Staffing</h3>
  <div class="bar"></div>
  <p>Years of Financial Planning and Analysis<br>experience across multiple industries can<br>help temporary&nbsp; staffing needs.</p>
  <div class="more">Learn More <svg width="14" height="14" viewBox="0 0 14 14"><circle cx="7" cy="7" r="7" fill="var(--blue)"/><path d="M5 4l3 3-3 3" stroke="#fff" stroke-width="2" fill="none"/></svg></div>
</div>

<!-- about -->
<section>
  <div class="abs about-bg"></div>
  <svg class="abs exp-panel" viewBox="0 0 452 451">
    <rect width="452" height="451" fill="var(--dark)"/>
    <polygon points="452,95 452,451 0,451" fill="var(--blue)"/>
  </svg>
  <div class="abs exp-num">10</div>
  <div class="abs exp-label">Years Of<br>Experience</div>
  <div class="abs profit"><b>$17</b><span>million in</span><span>profit</span></div>
  <h2 class="abs about-title">ABOUT KELVANE<br>CONSULTING</h2>
  <div class="abs about-quote">I am an experienced Finance professional who develops strategic financial plans, provides insightful analysis, and supports decision-making. With over 10 years of experience, I have successfully increased profitability for clients by $17M.</div>
  <div class="abs btn about-btn">LEARN MORE</div>
</section>

<!-- contact -->
<h2 class="abs section-title" style="top:2071px">CONTACT US</h2>

<div class="abs contact-item" style="top:2168px">
  <div class="contact-icon"><svg width="12" height="16" viewBox="0 0 12 16"><path d="M6 0a6 6 0 016 6c0 4.5-6 10-6 10S0 10.5 0 6a6 6 0 016-6z" fill="var(--blue)"/><circle cx="6" cy="6" r="2.2" fill="#fff"/></svg></div>
  <div><h4>Location</h4><p>112/b Kelvane Consulting. sit<br>amet, consectetur adipiscing</p></div>
</div>
<div class="abs contact-item" style="top:2280px">
  <div class="contact-icon"><svg width="15" height="15" viewBox="0 0 24 24"><path d="M6.6 10.8a15 15 0 006.6 6.6l2.2-2.2a1 1 0 011-.25 11.4 11.4 0 003.6.57 1 1 0 011 1V20a1 1 0 01-1 1A17 17 0 013 4a1 1 0 011-1h3.5a1 1 0 011 1c0 1.25.2 2.45.57 3.57a1 1 0 01-.25 1z" fill="var(--blue)"/></svg></div>
  <div><h4>Phone</h4><p>+1 555 014 2290</p></div>
</div>
<div class="abs contact-item" style="top:2368px">
  <div class="contact-icon"><svg width="14" height="11" viewBox="0 0 24 18"><rect width="24" height="18" rx="2" fill="var(--blue)"/><path d="M1 2l11 8 11-8" stroke="#fff" stroke-width="2" fill="none"/></svg></div>
  <div><h4>Email</h4><p>info@kelvaneconsulting.com</p></div>
</div>

<div class="abs field" style="top:2168px">Name</div>
<div class="abs field" style="top:2235px">Phone</div>
<div class="abs field" style="top:2302px">Email</div>
<div class="abs btn submit">Submit</div>
<div class="abs field field-message">Type your message</div>

<!-- footer -->
<footer>
  <svg class="abs" style="left:0;top:2497px" width="1200" height="704" viewBox="0 2497 1200 704">
    <rect x="0" y="2549" width="700" height="560" fill="var(--blue-light)"/>
    <polygon points="1200,2497 1200,3201 0,3201 0,3089 426,2702" fill="var(--black)"/>
  </svg>
  <div class="abs footer-logo"><div class="brand-mark"></div><div class="brand-name">KELVANE</div></div>
  <nav class="abs footer-links"><span>Terms &amp; conditions</span><span>Privacy Policy</span><span>About Us</span><span>Support</span></nav>
  <p class="abs copyright">Copyright© 2023 &nbsp;<u>Kelvane Consulting.</u> | &nbsp;All Rights Reserved</p>
  <div class="abs socials"><span aria-label="Social link"></span><span aria-label="Social link"></span><span aria-label="Social link"></span><span aria-label="Social link"></span></div>
</footer>

</body>
</html>
```